Brightway Haul & Repair Services, are a company that offers a 'one stop shop' pre-move clean up a

I have already selected a logo which I would like on the front of the business cards along with phone numbers, web address and email which are:
0419574302
www.brightwayhaul.com.au
brightwayhaulrepair@mailbox.example

On the back of the card I would like to list some of the types of service we offer (clean - move - repairs/maintenance) which are:
CLEAN - windows, gutters, solar panels, driveways/paths, carpets.
MOVE - Small/medium size house/office moves, large item pick-up & delivery, yard clean-up and removal.
General maintenance and repairs.

I would like the blue logo on a gray background.

Thanks

```html
<!DOCTYPE html>
<html lang="en">
<head>
<meta charset="utf-8">
<title>Brightway Haul &amp; Repair Services – Business Card</title>
<link href="https://fonts.googleapis.com/css2?family=Crimson+Text:wght@400;600&display=swap" rel="stylesheet">
<style>
  :root {
    --card-dark: #101010;
    --card-mid: #2b2b2b;
    --brand-blue: #2672f2;
    --brand-light: #8fd6ff;
    --title-navy: #0d2a78;
    --text-white: #ffffff;
    --text-soft: #e9e9e9;
    --divider: #ffffff;
  }
  * { margin: 0; padding: 0; box-sizing: border-box; }
  html, body {
    width: 1042px;
    height: 1200px;
    overflow: hidden;
    background: var(--divider);
    font-family: "Crimson Text", "Times New Roman", serif;
  }
  .canvas { position: relative; width: 1042px; height: 1200px; }
  .card {
    position: absolute;
    left: 0;
    width: 1042px;
    background: radial-gradient(ellipse at 50% 0%, var(--card-mid) 0%, var(--card-dark) 75%);
    overflow: hidden;
  }
  .card--front { top: 0; height: 596px; }
  .card--back { top: 603px; height: 597px; }

  .brand-name {
    position: absolute;
    top: 258px;
    left: 0;
    width: 100%;
    text-align: center;
    font-size: 58px;
    font-weight: 600;
    line-height: 1.1;
    color: var(--brand-light);
  }
  .brand-mark {
    position: absolute;
    top: 200px;
    left: 505px;
    width: 32px;
    height: 32px;
    background: var(--brand-blue);
  }

  .contact {
    position: absolute;
    top: 560px;
    left: 0;
    width: 100%;
    display: flex;
    justify-content: center;
    align-items: center;
    gap: 6px;
    font-size: 18.5px;
    color: var(--text-soft);
    white-space: nowrap;
  }
  .contact__icon { width: 17px; height: 17px; }
  .contact__sep { margin: 0 2px; }

  .service {
    position: absolute;
    width: 398px;
    height: 278px;
    border-radius: 50%;
    background: var(--brand-blue);
    box-shadow: 0 8px 14px rgba(0,0,0,0.75);
    display: flex;
    flex-direction: column;
    align-items: center;
    justify-content: center;
    text-align: center;
    color: var(--text-white);
    font-size: 25px;
    line-height: 1.14;
  }
  .service--clean { left: 78px; top: 145px; }
  .service--move { left: 589px; top: 145px; }
  .service__title {
    font-size: 30px;
    color: var(--title-navy);
    line-height: 1.05;
  }
  .service--clean .service__title { margin-top: -12px; }
  .service--move .service__title { margin-top: -36px; }

  .general-note {
    position: absolute;
    top: 535px;
    left: 0;
    width: 100%;
    text-align: center;
    font-size: 29px;
    color: var(--text-white);
  }
</style>
</head>
<body>
<main class="canvas">
  <section class="card card--front" aria-label="Card front">
    <span class="brand-mark" aria-hidden="true"></span>
    <h1 class="brand-name">Brightway Haul &amp; Repair Services</h1>
    <p class="contact">
      <svg class="contact__icon" viewBox="0 0 16 16" aria-hidden="true"><rect x="4" y="1" width="8" height="14" rx="1.5" fill="none" stroke="#ddd" stroke-width="1.3"/><rect x="5.5" y="3" width="5" height="4" fill="#ddd"/><circle cx="8" cy="12" r="1" fill="#ddd"/></svg>
      <span>0419574302</span><span class="contact__sep">|</span>
      <svg class="contact__icon" viewBox="0 0 20 16" aria-hidden="true" style="width:21px"><rect x="3" y="3" width="14" height="9" fill="none" stroke="#ddd" stroke-width="1.3"/><rect x="1" y="13" width="18" height="2" fill="#ddd"/></svg>
      <span>www.brightwayhaul.com.au</span><span class="contact__sep">|</span>
      <span>@brightwayhaulrepair@mailbox.example</span>
    </p>
  </section>

  <section class="card card--back" aria-label="Card back">
    <div class="service service--clean">
      <h2 class="service__title">CLEAN</h2>
      <p>windows, gutters,<br>solar panels,<br>driveways/paths, carpets</p>
    </div>
    <div class="service service--move">
      <h2 class="service__title">MOVE</h2>
      <p>Small/medium size house/<br>office moves,<br>large item pick-up &amp; delivery,<br>yard clean-up and removal</p>
    </div>
    <p class="general-note">General maintenance and repairs.</p>
  </section>
</main>
</body>
</html>
```